Beer Can Label design - HAZY NEIPA

Hazy NEIPA. (Acronym for New England India Pale Ale)
Full sleeve (473ml)
5.00" x 8.125" Inches
Write up on can reverse.
Opaque haze in appearance derived from specific oats, wheat, and water chemistry. This brew bolsters a dense and creamy head, leaving behind a soft and silky mouth-feel. Expect an intense tropical fruit centric aroma and flavour. Our timely hop additions contributes to less bitterness than typical IPA’s.
Logo is to be on front, towards bottom. Title near top.
Looking for something that stands out. Bold.
Target Market(s)
Craft beer enthusiasts
Industry/Entity Type
Beer & Brewing
Requirements
Must have
- Eye catching.

```html
<!DOCTYPE html>
<html lang="en">
<head>
<meta charset="utf-8">
<title>Hazy NEIPA – Can Label Variants</title>
<link href="https://fonts.googleapis.com/css2?family=Baloo+2:wght@500;600;800&family=Fredoka:wght@600&family=Permanent+Marker&family=Nunito:wght@800&display=swap" rel="stylesheet">
<style>
  :root {
    --page: #efefef;
    --teal: #17765f;
    --teal-dark: #0f5a48;
    --leaf: #7cbf2e;
    --leaf-light: #9fd24a;
    --white: #ffffff;
    --lime: #c6da3c;
    --lime-deep: #a9c526;
    --green: #5dbd28;
    --green-deep: #3f9a1b;
    --yellow: #e4ea1c;
    --caption: #b3b3b3;
    --hop: #3d7a2a;
  }
  * { box-sizing: border-box; margin: 0; padding: 0; }
  html, body { width: 1200px; height: 750px; overflow: hidden; }
  body { background: var(--page); font-family: "Baloo 2", sans-serif; position: relative; }

  .label {
    position: absolute; top: 140px; width: 200px; height: 500px;
    border-radius: 6px; overflow: hidden;
  }
  .label--main { left: 200px; background: linear-gradient(90deg, #e6e7ea, #ffffff 40%, #e9eaec); }
  .label--reversed { left: 490px; background: linear-gradient(90deg, var(--lime), #d5e35a 35%, var(--lime-deep)); }
  .label--alternate { left: 780px; background: linear-gradient(90deg, var(--green), #8fd64b 35%, var(--green-deep)); }

  .label__pattern { position: absolute; inset: 0; opacity: .35; }
  .label--main .label__pattern { background: radial-gradient(circle at 10% 30%, #b9dd6a 0 18px, transparent 19px), radial-gradient(circle at 95% 60%, #2f9c7c 0 14px, transparent 15px); }
  .label--reversed .label__pattern { background: radial-gradient(circle at 4% 50%, #2a9c86 0 12px, transparent 13px), radial-gradient(circle at 98% 30%, #2a9c86 0 10px, transparent 11px); }
  .label--alternate .label__pattern { background: radial-gradient(circle at 4% 40%, #e4ea1c 0 14px, transparent 15px), radial-gradient(circle at 98% 55%, #1e6e2e 0 14px, transparent 15px); }

  .label__hop {
    position: absolute; left: 77px; top: 48px; width: 46px; height: 56px;
    border-radius: 50% 50% 46% 46%;
    background: radial-gradient(circle at 40% 35%, #6aa83a, var(--hop));
  }

  .label__title {
    position: absolute; left: 14px; top: 108px; width: 180px;
    font-family: "Baloo 2", sans-serif; font-weight: 800; font-size: 68px;
    line-height: 1; letter-spacing: -1px;
  }
  .label--main .label__title { color: var(--leaf); }
  .label--reversed .label__title, .label--alternate .label__title { color: var(--white); }

  .label__style {
    position: absolute; left: 14px; top: 172px; width: 124px; height: 30px;
    background: var(--teal); border-radius: 4px 12px 12px 4px;
    font-family: "Fredoka", sans-serif; font-weight: 600; font-size: 26px;
    color: var(--white); line-height: 28px; padding-left: 10px;
  }
  .label__tagline {
    position: absolute; left: 146px; top: 172px; width: 52px;
    font-family: "Permanent Marker", cursive; font-size: 10px; line-height: 1.15;
    color: var(--teal);
  }

  .label__body {
    position: absolute; left: 30px; top: 258px; width: 150px;
    font-size: 7.4px; line-height: 1.42; font-weight: 500; color: var(--teal);
  }
  .label--alternate .label__body { color: var(--white); }

  .label__producer {
    position: absolute; left: 30px; top: 396px;
    font-family: "Permanent Marker", cursive; font-size: 10px; color: var(--leaf);
  }
  .label--reversed .label__producer, .label--alternate .label__producer { color: var(--white); }

  .brewery {
    position: absolute; left: 26px; top: 416px; display: flex; align-items: center; gap: 5px;
  }
  .brewery__dot { width: 14px; height: 14px; border-radius: 50%; background: var(--teal-dark); }
  .brewery__name {
    font-weight: 800; font-size: 10px; line-height: 1.05; color: var(--teal-dark); width: 68px;
  }

  .label__specs {
    position: absolute; right: 22px; top: 424px; text-align: right;
    font-weight: 800; color: var(--teal); line-height: 1.15;
  }
  .label--alternate .label__specs { color: var(--yellow); }
  .label__specs .num { font-size: 12px; }
  .label__specs .unit { font-size: 8px; }

  .caption {
    position: absolute; top: 705px; width: 200px; text-align: center;
    font-family: "Nunito", sans-serif; font-weight: 800; font-size: 16px;
    letter-spacing: 1px; color: var(--caption);
  }
</style>
</head>
<body>

  <section class="label label--main">
    <div class="label__pattern" role="img" aria-label="Hand-drawn tropical fruit and leaf pattern"></div>
    <div class="label__hop" role="img" aria-label="Hop cone illustration"></div>
    <h1 class="label__title">HAZY</h1>
    <div class="label__style">neipa</div>
    <p class="label__tagline">FOR ALL HOP HEADS!</p>
    <p class="label__body">Opaque haze in appearance derived from specific oats, wheat, and water chemistry. This brew bolsters a dense and creamy head, leaving behind a soft and silky mouth-feel. Expect an intense tropical fruit centric aroma and flavour. Our timely hop additions contributes to less bitterness than typical IPA’s.</p>
    <p class="label__producer">PRODUCED BY:</p>
    <div class="brewery"><span class="brewery__dot"></span><span class="brewery__name">HARBOR LANE BREW HOUSE</span></div>
    <p class="label__specs"><span class="num">473</span><span class="unit">ml</span><br><span class="num">21.5%</span><span class="unit">alv</span></p>
  </section>

  <section class="label label--reversed">
    <div class="label__pattern" role="img" aria-label="Hand-drawn tropical fruit and leaf pattern"></div>
    <div class="label__hop" role="img" aria-label="Hop cone illustration"></div>
    <h1 class="label__title">HAZY</h1>
    <div class="label__style">neipa</div>
    <p class="label__tagline">FOR ALL HOP HEADS!</p>
    <p class="label__body">Opaque haze in appearance derived from specific oats, wheat, and water chemistry. This brew bolsters a dense and creamy head, leaving behind a soft and silky mouth-feel. Expect an intense tropical fruit centric aroma and flavour. Our timely hop additions contributes to less bitterness than typical IPA’s.</p>
    <p class="label__producer">PRODUCED BY:</p>
    <div class="brewery"><span class="brewery__dot"></span><span class="brewery__name">HARBOR LANE BREW HOUSE</span></div>
    <p class="label__specs"><span class="num">473</span><span class="unit">ml</span><br><span class="num">21.5%</span><span class="unit">alv</span></p>
  </section>

  <section class="label label--alternate">
    <div class="label__pattern" role="img" aria-label="Hand-drawn tropical fruit and leaf pattern"></div>
    <div class="label__hop" role="img" aria-label="Hop cone illustration"></div>
    <h1 class="label__title">HAZY</h1>
    <div class="label__style">neipa</div>
    <p class="label__tagline">FOR ALL HOP HEADS!</p>
    <p class="label__body">Opaque haze in appearance derived from specific oats, wheat, and water chemistry. This brew bolsters a dense and creamy head, leaving behind a soft and silky mouth-feel. Expect an intense tropical fruit centric aroma and flavour. Our timely hop additions contributes to less bitterness than typical IPA’s.</p>
    <p class="label__producer">PRODUCED BY:</p>
    <div class="brewery"><span class="brewery__dot"></span><span class="brewery__name">HARBOR LANE BREW HOUSE</span></div>
    <p class="label__specs"><span class="num">473</span><span class="unit">ml</span><br><span class="num">21.5%</span><span class="unit">alv</span></p>
  </section>

  <p class="caption" style="left:200px">MAIN</p>
  <p class="caption" style="left:490px">REVERSED</p>
  <p class="caption" style="left:780px">ALTERNATE</p>

</body>
</html>
```